Trade Exhibition and Conference Prospectus

BRELOM is an industry Association. We hold a large trade show and conference each year. We need an engaging exhibition prospectus to send to potential exhibitors.

We represent the amusement, leisure and recreation industries in Australia and we focus these events on being fun and educational for business owners

We would like to see colours matching our corporate colours as seen in our logo.

We would like to design to be highly professional as well as conveying a sense of fun and excitement.

I have included an example of what we have done in the past. I would like to improve on this dramatically

Industry/Entity Type

Industry

```html
<!DOCTYPE html>
<html lang="en">
<head>
<meta charset="utf-8">
<title>BRELOM Exhibition Prospectus</title>
<link href="https://fonts.googleapis.com/css2?family=Open+Sans:ital,wght@0,400;0,600;0,700;0,800;1,400&display=swap" rel="stylesheet">
<style>
  :root {
    --orange: #f5a623;
    --orange-deep: #f39a1e;
    --orange-light: #f8b94a;
    --yellow: #fcc12d;
    --blue: #1f6fc1;
    --green: #5db043;
    --ink: #2b2b2b;
    --grey-text: #555555;
    --paper: #ffffff;
    --stage: #d6d6d8;
  }
  * { box-sizing: border-box; margin: 0; padding: 0; }
  html, body { width: 1200px; height: 849px; overflow: hidden; }
  body {
    background: radial-gradient(ellipse at 50% 40%, #f0f0f1 0%, var(--stage) 100%);
    font-family: "Open Sans", Arial, sans-serif;
    color: var(--ink);
    position: relative;
  }
  .prospectus {
    position: absolute; left: 40px; top: 125px;
    width: 1120px; height: 600px;
    background: var(--paper);
    box-shadow: 0 10px 30px rgba(0,0,0,0.18);
    overflow: hidden;
  }
  .prospectus__shapes { position: absolute; inset: 0; }
  .fold {
    position: absolute; top: 0; bottom: 0; width: 1px;
    background: rgba(0,0,0,0.06);
  }
  .block { position: absolute; }

  /* Panel 1 */
  .invite { left: 22px; top: 22px; width: 240px; color: #fff; }
  .invite__title { font-size: 24px; font-weight: 600; line-height: 1.1; margin-bottom: 10px; }
  .invite p { font-size: 8.5px; line-height: 1.45; margin-bottom: 6px; font-weight: 600; }
  .brand {
    left: 22px; top: 248px; display: flex; align-items: center; gap: 8px;
    color: rgba(255,255,255,0.8); font-weight: 700; font-size: 18px; letter-spacing: 2px;
  }
  .brand__dot { width: 12px; height: 12px; border-radius: 50%; background: rgba(255,255,255,0.8); }
  .exhibit { left: 22px; top: 355px; width: 240px; }
  .exhibit__title { font-size: 12px; font-weight: 700; margin-bottom: 8px; text-align: right; }

  .category { margin-bottom: 8px; }
  .category h3 { font-size: 8.5px; font-weight: 800; text-transform: uppercase; line-height: 1.25; }
  .category p { font-size: 7.5px; line-height: 1.35; color: var(--grey-text); }

  /* Panels 2 and 3 */
  .list-col { top: 20px; }
  .list-col--a { left: 392px; width: 160px; }
  .list-col--c { left: 580px; width: 188px; }

  .photo { position: absolute; }
  .photo--crowd {
    left: 280px; top: 470px; width: 500px; height: 130px;
    background: linear-gradient(100deg, #6d5444 0%, #a88f7a 35%, #c9b8a6 55%, #7c6a5c 80%, #3f4f7a 100%);
  }
  .photo--staff {
    left: 780px; top: 20px; width: 60px; height: 290px;
    background: linear-gradient(180deg, #e5862d 0%, #b5312a 55%, #7a2a2a 100%);
  }

  /* Panel 4 */
  .invest { left: 860px; top: 22px; width: 240px; }
  .invest__title { color: var(--orange); font-size: 12px; font-weight: 800; text-transform: uppercase; }
  .invest__sub { color: var(--orange); font-size: 10px; font-weight: 800; text-transform: uppercase; margin: 2px 0 6px; }
  .invest__label { font-size: 7.5px; font-weight: 800; text-transform: uppercase; margin-bottom: 3px; }
  .invest ul { list-style: none; font-size: 7px; line-height: 1.4; color: var(--grey-text); width: 115px; }
  .invest__note { font-size: 7px; color: var(--grey-text); width: 115px; margin-top: 6px; line-height: 1.4; }
  .floorplan {
    position: absolute; left: 985px; top: 110px; width: 115px; height: 110px;
    background: linear-gradient(135deg, #f4f4f4, #e2e2e2);
    border: 1px solid #9a9a9a;
  }
  .catering { left: 985px; top: 230px; width: 115px; font-size: 7px; color: var(--grey-text); line-height: 1.4; }
  .catering strong { color: var(--ink); font-size: 7.5px; text-transform: uppercase; }
  .photo--coast {
    left: 870px; top: 320px; width: 190px; height: 95px;
    background: linear-gradient(180deg, #8ec3e8 0%, #d9e6ee 45%, #2f7fb2 75%, #e3d3b1 100%);
  }
  .marketing { left: 860px; top: 430px; width: 200px; }
  .marketing__title { color: var(--orange); font-size: 11px; font-weight: 800; text-transform: uppercase; margin-bottom: 5px; }
  .marketing ul { list-style: none; font-size: 7px; line-height: 1.45; color: var(--grey-text); }
</style>
</head>
<body>
  <main class="prospectus">
    <svg class="prospectus__shapes" viewBox="0 0 1120 600" width="1120" height="600" aria-hidden="true">
      <polygon points="0,0 280,0 280,300 0,330" fill="var(--orange)"/>
      <polygon points="0,0 140,0 0,210" fill="var(--orange-light)"/>
      <polygon points="140,0 280,0 280,300 0,330 0,210" fill="var(--yellow)" opacity="0.55"/>
      <polygon points="280,0 380,0 280,100" fill="var(--orange-deep)"/>
      <polygon points="225,312 280,262 280,345" fill="var(--green)"/>
      <polygon points="620,470 840,290 840,375 735,470" fill="var(--blue)"/>
      <polygon points="1065,600 1120,430 1120,600" fill="var(--green)"/>
    </svg>

    <div class="fold" style="left:280px"></div>
    <div class="fold" style="left:560px"></div>
    <div class="fold" style="left:840px"></div>

    <section class="block invite">
      <h1 class="invite__title">Your invitation to attend...</h1>
      <p>Be part of Australia's only attractions, amusement and leisure industry exhibition, bringing together operators, suppliers and manufacturers.</p>
      <p>This trade event is a cost effective way to meet key buyers, launch new products and grow your network with decision makers from the whole leisure sector across the nation at this important event.</p>
    </section>

    <div class="block brand"><span class="brand__dot"></span>BRELOM</div>

    <section class="block exhibit">
      <h2 class="exhibit__title">Who Should Exhibit</h2>
      <div class="category"><h3>Access Control</h3><p>Ticketing, point of sale, RFID, turnstiles, wristbands.</p></div>
      <div class="category"><h3>Admission Systems and Devices</h3><p>Turnstiles, gates, counters, ticket printers.</p></div>
      <div class="category"><h3>Amusement Rides and Attractions</h3><p>Carousels, dark rides, bumper cars, family rides, trains and ride parts.</p></div>
      <div class="category"><h3>Arcade Games and Coin Operated</h3><p>Arcade machines, redemption prizes, kiddie rides, midway skills.</p></div>
    </section>

    <section class="block list-col list-col--a">
      <div class="category"><h3>Aquatic Leisure</h3><p>Aquatic play rides and attractions, flumes, rafts, wave machines, water treatment.</p></div>
      <div class="category"><h3>Clothing</h3><p>Costumes, swimwear, resort wear, t-shirts, uniforms.</p></div>
      <div class="category"><h3>Computer Systems / Software</h3><p>Line management systems, point of sale, ride control systems.</p></div>
      <div class="category"><h3>Consultants</h3><p>Accounting, advertising, public relations, architecture, design, engineering, feasibility, insurance, legal, research.</p></div>
      <div class="category"><h3>Display and Theming and Show Productions</h3><p>Animatronics, special effects, simulation, virtual reality, lighting and laser shows.</p></div>
      <div class="category"><h3>Food and Beverage Suppliers</h3><p>Food preparation equipment, beverages, confectionery.</p></div>
    </section>

    <section class="block list-col list-col--c">
      <div class="category"><p>Popcorn, pretzels, snack foods, carts and kiosks, vending machines.</p></div>
      <div class="category"><h3>Facility and Grounds</h3><p>Awnings, canopies, seating, turf, fencing, lighting, landscaping and maintenance supplies.</p></div>
      <div class="category"><h3>Indoor Play and Participatory Play</h3><p>Play structures, family entertainment centres, ropes courses, laser tag, mini golf.</p></div>
      <div class="category"><h3>People-Moving Equipment</h3><p>Carts, golf carts, strollers, trams and mobility aids.</p></div>
      <div class="category"><h3>Photographic Equipment</h3><p>Equipment and supplies, photo booths, ride photography.</p></div>
      <div class="category"><h3>Security Equipment and Safety</h3><p>Cameras, surveillance, fire systems, traffic controls.</p></div>
    </section>

    <div class="photo photo--crowd" role="img" aria-label="Photo of visitors and exhibitors meeting on the trade show floor"></div>
    <div class="photo photo--staff" role="img" aria-label="Photo of an exhibitor at a colourful candy stand"></div>

    <section class="block invest">
      <h2 class="invest__title">Exhibitor Investment</h2>
      <h3 class="invest__sub">Exhibitor Trade Booth Package</h3>
      <p class="invest__label">Trade booth includes:</p>
      <ul>
        <li>• 3m x 3m shell scheme booth</li>
        <li>• Back and side walls</li>
        <li>• Company name fascia sign</li>
        <li>• Two spotlights per booth</li>
        <li>• One power outlet</li>
        <li>• Carpet floor covering</li>
        <li>• Two exhibitor passes</li>
      </ul>
      <p class="invest__note">Prices exclude GST. Larger spaces and raw floor space available on request.</p>
    </section>

    <div class="floorplan" role="img" aria-label="Floor plan of the exhibition hall booth layout"></div>

    <div class="block catering"><strong>Catering package includes:</strong><br>Morning and afternoon tea and lunch for two staff on each day of the exhibition.</div>

    <div class="photo photo--coast" role="img" aria-label="Photo of a coastal city skyline and beach"></div>

    <section class="block marketing">
      <h2 class="marketing__title">Marketing and Publicity Support</h2>
      <ul>
        <li>• One A4 promotional flyer inserted into delegate registration packs</li>
        <li>• Company listing in the show guide and event website</li>
        <li>• Promotion of your company in the BRELOM e-newsletter</li>
        <li>• Free entry to all conference education sessions</li>
        <li>• One full page colour advertisement in the BRELOM Member and Industry Supplier directory</li>
      </ul>
    </section>
  </main>
</body>
</html>
```